Velvet Harbour Sessions

Need to improve polish and professionalism of PPT presentation. Get consistent look and feel through whole slides, improved look and feel while maintaining the corporate standards/colour scheme, from the Brimwells corporate presentation. Need everything in Arial font with colours consistent with the PPT template

```html
<!DOCTYPE html>
<html lang="en">
<head>
<meta charset="utf-8">
<title>Velvet Harbour Sessions – KPIs &amp; Production Fundamentals</title>
<link rel="stylesheet" href="https://fonts.googleapis.com/css2?family=Fira+Sans:wght@800&family=Open+Sans:wght@400;600;700&display=swap">
<style>
:root{
  --ink:#1c2b36;
  --teal-dark:#122c35;
  --teal:#1d3f4a;
  --footer:#152f39;
  --accent:#d3282e;
  --cal:#1f2d5c;
  --avail:#243f86;
  --op:#2f55a6;
  --eff:#6b8fcd;
  --neff:#7030a0;
  --delay:#4e9a2c;
  --stby:#f8bd3a;
  --down:#d3282e;
  --slate:#5d6b73;
  --node-dark:#1b2a30;
  --page:#ffffff;
}
*{margin:0;padding:0;box-sizing:border-box}
html,body{width:1200px;height:2194px;overflow:hidden;background:var(--page)}
body{position:relative;font-family:"Open Sans",Arial,sans-serif;color:var(--ink)}

.slide{position:absolute;width:542px;height:304px;background:#fff;overflow:hidden;box-shadow:0 6px 18px rgba(0,0,0,.22)}
.col-l{left:43px}.col-r{left:614px}
.row-1{top:178px}.row-2{top:561px}.row-3{top:945px}.row-4{top:1328px}.row-5{top:1711px}

.photo{position:absolute;left:0;top:0;width:100%}
.photo-mine{background:linear-gradient(160deg,#1e4450 0%,#163540 55%,#0f2730 100%)}
.photo-tunnel{background:linear-gradient(100deg,#2a2e2c 0%,#1d3a42 45%,#41525a 75%,#1a3039 100%)}
.photo-truck{background:linear-gradient(180deg,#234550 0%,#183944 100%)}

.footer{position:absolute;left:0;bottom:0;width:100%;height:15px;background:var(--footer)}
.footer .brand{position:absolute;left:14px;top:2px;color:#fff;font-weight:700;font-size:8.5px;letter-spacing:.4px;display:flex;align-items:center;gap:3px}
.brand .dot{width:4px;height:4px;background:var(--accent);border-radius:50%}
.footer .legal{position:absolute;left:0;right:0;top:4px;text-align:center;color:#c9d3d6;font-size:4.6px}
.footer .num{position:absolute;right:15px;top:0;width:23px;height:15px;background:var(--accent);color:#fff;font-size:5.5px;text-align:center;line-height:15px}

.slide-title{position:absolute;left:0;right:0;text-align:center;font-family:"Fira Sans",Arial,sans-serif;font-weight:800;font-size:20px;color:var(--ink)}
.on-dark{color:#fff}

ul.points{position:absolute;list-style:none;font-size:8.2px;line-height:1.2}
ul.points li{position:relative;padding-left:11px;margin-bottom:2.5px}
ul.points li::before{content:"";position:absolute;left:1px;top:3px;width:4px;height:4px;border:1px solid var(--ink)}
ul.points ul{list-style:none;margin-top:1.5px}
ul.points ul li{font-size:6.6px;margin-bottom:1.5px}
ul.points ul li::before{top:2px;width:3.5px;height:3.5px}
ul.points.tight li{margin-bottom:1px}
b{font-weight:700}

/* time usage model */
.tum{position:absolute;left:18px;width:506px}
.cell{position:absolute;display:flex;flex-direction:column;align-items:center;justify-content:center;color:#fff;text-align:center;font-size:10px;line-height:1.05}
.cell small{font-size:5.6px;margin-top:1px;opacity:.9}
.cell.muted{color:#eef2fa}
.r-cal{top:0;height:28px}.r-avail{top:28px;height:30px}.r-half{top:58px;height:38px}.r-low{top:96px;height:42px}.r-full{top:58px;height:80px}
.c-cal{left:0;width:506px;background:var(--cal)}
.c-avail{left:0;width:337px;background:var(--avail)}
.c-down{left:337px;width:169px;background:var(--down)}
.c-op{left:0;width:169px;background:var(--op)}
.c-eff{left:0;width:84px;background:var(--eff)}
.c-neff{left:84px;width:85px;background:var(--neff)}
.c-delay{left:169px;width:84px;background:var(--delay)}
.c-stby{left:253px;width:84px;background:var(--stby);color:#fff8e6}
.c-un1{left:337px;width:84px;background:var(--down)}
.c-un2{left:421px;width:85px;background:var(--down)}

/* process diagram */
.node{position:absolute;display:flex;align-items:center;justify-content:center;text-align:center;color:#fff;font-size:9px;line-height:1.15;border-radius:6px;box-shadow:0 3px 6px rgba(0,0,0,.3)}
.node-prod{left:172px;top:66px;width:198px;height:42px;background:var(--accent)}
.node-equip{left:134px;top:129px;width:112px;height:42px;background:var(--node-dark)}
.node-time{left:295px;top:130px;width:112px;height:41px;background:var(--slate)}
.links{position:absolute;left:0;top:0}
.lead{position:absolute;left:0;right:0;text-align:center;color:#fff;font-weight:700;font-size:9px}
</style>
</head>
<body>

<!-- 1 Cover -->
<section class="slide col-l row-1">
  <div class="photo photo-mine" style="height:304px" role="img" aria-label="Dark teal-toned aerial view of an open-pit mine"></div>
  <div style="position:absolute;left:24px;top:26px;display:flex;align-items:center;gap:6px;color:#fff;font-weight:700;font-size:26px;letter-spacing:1px">BRIMWELLS<span style="width:7px;height:7px;background:var(--accent);border-radius:50%"></span></div>
  <h1 style="position:absolute;left:26px;top:116px;color:#fff;font-family:'Fira Sans',Arial,sans-serif;font-weight:800;font-size:20.5px;line-height:1.22">Velvet Harbour Sessions<br>KPIs &amp; Production Fundamentals</h1>
  <p style="position:absolute;right:18px;top:268px;text-align:right;color:#fff;font-weight:700;font-size:5px;line-height:1.5">© 2024 Brimwells Mining Solutions Inc.<br>Strictly Confidential</p>
</section>

<!-- 2 Objectives -->
<section class="slide col-r row-1">
  <div class="photo photo-mine" style="width:243px;height:289px" role="img" aria-label="Dark teal-toned view of a mine site"></div>
  <h2 style="position:absolute;left:0;width:243px;top:128px;text-align:center;color:#fff;font-family:'Fira Sans',Arial,sans-serif;font-weight:800;font-size:19px;line-height:1.15">KPI &amp; Production<br>Fundamentals</h2>
  <p style="position:absolute;left:257px;top:48px;font-weight:700;font-size:9.3px">At the end of this module, you will understand</p>
  <ul class="points" style="left:256px;top:64px;width:270px;font-size:7.6px;font-weight:700">
    <li>Understand the key concepts of mine production KPIs
      <ul style="font-weight:400;margin-left:9px">
        <li>Time Usage Model</li>
        <li>Availability, Utilization and Productivity</li>
        <li>Elements of the haul cycle</li>
        <li>Elements of the loading cycle</li>
        <li>How changes in each of these elements impact mine production</li>
      </ul>
    </li>
    <li style="margin-top:14px">The goal will be to create a baseline of understanding and a common language across the entire mine-ops team</li>
    <li style="margin-top:4px">You may already understand these concepts</li>
    <li style="margin-top:4px">This is the time to ask questions and get clarification!</li>
  </ul>
  <footer class="footer"><span class="brand">BRIMWELLS<span class="dot"></span></span><span class="legal">© 2024 Brimwells Mining Solutions Inc. Strictly Confidential</span><span class="num">2</span></footer>
</section>

<!-- 3 Production -->
<section class="slide col-l row-2">
  <div class="photo photo-tunnel" style="height:152px" role="img" aria-label="Underground mine tunnel with equipment"></div>
  <h2 class="slide-title on-dark" style="top:10px">What Makes up Production</h2>
  <p class="lead" style="top:48px">In its simplest terms, we calculate production like this:</p>
  <svg class="links" width="542" height="152"><path d="M271 108v10M189 130v-12h161v12" fill="none" stroke="#d3282e" stroke-width="1.2"/></svg>
  <div class="node node-prod">Production</div>
  <div class="node node-equip">Equipment<br>Productivity</div>
  <div class="node node-time">Operating Time</div>
  <ul class="points" style="left:51px;top:182px;width:470px;font-size:8.8px">
    <li><b>This is true for any process</b>
      <ul><li>Mowing the lawn</li><li>Driving</li><li>Mine Production</li></ul>
    </li>
    <li>Production goes up or down because of a change in <b>Equipment Productivity</b> or <b>Operating Time</b></li>
  </ul>
  <footer class="footer"><span class="brand">BRIMWELLS<span class="dot"></span></span><span class="legal">© 2024 Brimwells Mining Solutions Inc. Strictly Confidential</span><span class="num">3</span></footer>
</section>

<!-- 4 Production detail -->
<section class="slide col-r row-2">
  <div class="photo photo-truck" style="height:152px" role="img" aria-label="Teal-toned photo of a mine haul truck"></div>
  <h2 class="slide-title on-dark" style="top:10px">What Makes up Production</h2>
  <p class="lead" style="top:43px;font-size:9.6px;font-weight:600">At its simplest terms, we calculate production like this:</p>
  <svg class="links" width="542" height="152"><path d="M271 108v10M189 130v-12h161v12" fill="none" stroke="#d3282e" stroke-width="1.2"/></svg>
  <div class="node node-prod">Production</div>
  <div class="node node-equip">Equipment<br>Productivity</div>
  <div class="node node-time">Operating Time</div>
  <ul class="points" style="left:53px;top:194px;width:470px;font-size:8.8px;line-height:1.05">
    <li style="margin-bottom:6px">Operating time is the time when a piece of equipment is performing it’s <b>primary function</b></li>
    <li style="margin-bottom:6px">To better understand, communicate and discuss the different categories of how we calculate operating time, we use something called a <b>Time Usage Model</b></li>
    <li style="margin-bottom:6px">Each industry has its own time usage model, and they can vary slightly from industry to industry</li>
    <li>Even within an industry, (e.g. Mining) a Time Usage Model can vary from operation to operation</li>
  </ul>
  <footer class="footer"><span class="brand">BRIMWELLS<span class="dot"></span></span><span class="legal">© 2024 Brimwells Mining Solutions Inc. Strictly Confidential</span><span class="num">4</span></footer>
</section>

<!-- 5 Generic TUM -->
<section class="slide col-l row-3">
  <h2 class="slide-title" style="top:9px">Generic Time Usage Model</h2>
  <div class="tum" style="top:49px;height:138px">
    <div class="cell r-cal c-cal">Calendar Time<small>0d 12 h 0 min</small></div>
    <div class="cell r-avail c-avail">Available Time<small>0d 12 h 0 min</small></div>
    <div class="cell r-avail c-down">Down<small>0d 12 h 0 min</small></div>
    <div class="cell r-half c-op">Operating Time<small>0d 12 h 0 min</small></div>
    <div class="cell r-low c-eff muted">Efective Time<small>0d 12 h 0 min</small></div>
    <div class="cell r-low c-neff">NonEffective Time<small>0d 12 h 0 min</small></div>
    <div class="cell r-full c-delay">Operating Delay<small>0d 12 h 0 min</small></div>
    <div class="cell r-full c-stby">Standby Time<small>0d 12 h 0 min</small></div>
    <div class="cell r-full c-un1">Unscheduled<small>0d 12 h 0 min</small></div>
    <div class="cell r-full c-un2">Unscheduled<small>0d 12 h 0 min</small></div>
  </div>
  <ul class="points" style="left:41px;top:209px;width:470px;font-size:7.8px;line-height:1.1">
    <li style="margin-bottom:4px">This is a generic Mining time usage model</li>
    <li>There may be variations from mine-to-mine (ie Utilized time vs Operating Time) but this model describes everything mine operations needs to know about the time usage of a piece of equipment</li>
  </ul>
  <footer class="footer"><span class="brand">BRIMWELLS<span class="dot"></span></span><span class="legal">© 2024 Brimwells Mining Solutions Inc. Strictly Confidential</span><span class="num">5</span></footer>
</section>

<!-- 6 Calendar Time -->
<section class="slide col-r row-3">
  <div class="photo photo-truck" style="height:135px" role="img" aria-label="Teal-toned photo of a large haul truck"></div>
  <h2 class="slide-title on-dark" style="top:52px">TUM – Calendar Time</h2>
  <div class="tum" style="top:152px;height:28px">
    <div class="cell r-cal c-cal">Calendar Time<small>0d 12 h 0 min</small></div>
  </div>
  <p style="position:absolute;left:0;right:0;top:200px;text-align:center;font-weight:700;font-size:9.2px">Calendar time means all the time in a period</p>
  <ul class="points" style="left:176px;top:214px;width:230px;font-size:8px">
    <li style="margin-bottom:1.5px">Calendar time for 1 Year = 365 Days</li>
    <li style="margin-bottom:1.5px">Calendar time for October = 31 days</li>
    <li>Calendar time for 1 shift = 12 hours</li>
  </ul>
  <footer class="footer"><span class="brand">BRIMWELLS<span class="dot"></span></span><span class="legal">© 2024 Brimwells Mining Solutions Inc. Strictly Confidential</span><span class="num">6</span></footer>
</section>

<!-- 7 Available Time -->
<section class="slide col-l row-4">
  <h2 class="slide-title" style="top:9px">TUM – Available Time</h2>
  <div class="tum" style="top:60px;height:58px">
    <div class="cell r-cal c-cal">Calendar Time<small>0d 12 h 0 min</small></div>
    <div class="cell r-avail c-avail">Available Time<small>0d 12 h 0 min</small></div>
    <div class="cell r-avail c-down">Down<small>0d 12 h 0 min</small></div>
  </div>
  <p style="position:absolute;left:53px;top:124px;font-size:8px"><b>Available Time</b> is the time a piece of equipment (or fleet) is mechanically available to operate</p>
  <ul class="points" style="left:53px;top:138px;width:430px;font-size:8px">
    <li style="margin-left:9px;margin-bottom:4px">Available Time = Calendar Time – Down Time</li>
    <li style="margin-left:9px">Downtime can be
      <ul><li>Planned (PMs, Rebuilds)</li><li>Unplanned (Breakdown, Accident Damage)</li></ul>
    </li>
    <li>Availability % = Available Time / Calendar Time</li>
  </ul>
  <footer class="footer"><span class="brand">BRIMWELLS<span class="dot"></span></span><span class="legal">© 2024 Brimwells Mining Solutions Inc. Strictly Confidential</span><span class="num">7</span></footer>
</section>

<!-- 8 Available Time detail -->
<section class="slide col-r row-4">
  <h2 class="slide-title" style="top:9px">TUM – Available Time</h2>
  <div class="tum" style="top:64px;height:140px">
    <div class="cell r-cal c-cal">Calendar Time<small>0d 12 h 0 min</small></div>
    <div class="cell r-avail c-avail">Available Time<small>0d 12 h 0 min</small></div>
    <div class="cell r-avail c-down">Down<small>0d 12 h 0 min</small></div>
    <div class="cell c-un1" style="top:58px;height:82px">Unscheduled<small>0d 12 h 0 min</small></div>
    <div class="cell c-un2" style="top:58px;height:82px">Unscheduled<small>0d 12 h 0 min</small></div>
  </div>
  <p style="position:absolute;left:49px;top:136px;font-size:7.8px"><b>Available Time</b> is the time a piece of equipment</p>
  <ul class="points" style="left:49px;top:150px;width:300px;font-size:7.8px">
    <li style="margin-bottom:4px">(or fleet) is mechanically available to operate</li>
    <li style="margin-bottom:4px">Available Time = Calendar Time – Down Time</li>
    <li>Downtime can be
      <ul><li>Planned (PMs, Rebuilds)</li><li>Unplanned (Breakdown, Accident Damage)</li></ul>
    </li>
    <li>Availability % = Available Time / Calendar Time</li>
  </ul>
  <footer class="footer"><span class="brand">BRIMWELLS<span class="dot"></span></span><span class="legal">© 2024 Brimwells Mining Solutions Inc. Strictly Confidential</span><span class="num">8</span></footer>
</section>

<!-- 9 Effective Time -->
<section class="slide col-l row-5">
  <h2 class="slide-title" style="top:9px">TUM – Effective Time</h2>
  <div class="tum" style="top:44px;height:138px">
    <div class="cell r-cal c-cal">Calendar Time<small>0d 12 h 0 min</small></div>
    <div class="cell r-avail c-avail">Available Time<small>0d 12 h 0 min</small></div>
    <div class="cell r-avail c-down">Down<small>0d 12 h 0 min</small></div>
    <div class="cell r-half c-op">Operating Time<small>0d 12 h 0 min</small></div>
    <div class="cell r-low c-eff muted">Efective Time<small>0d 12 h 0 min</small></div>
    <div class="cell r-low c-neff">NonEffective Time<small>0d 12 h 0 min</small></div>
    <div class="cell r-full c-delay">Operating Delay<small>0d 12 h 0 min</small></div>
    <div class="cell r-full c-stby">Standby Time<small>0d 12 h 0 min</small></div>
    <div class="cell r-full c-un1">Unscheduled<small>0d 12 h 0 min</small></div>
    <div class="cell r-full c-un2">Unscheduled<small>0d 12 h 0 min</small></div>
  </div>
  <ul class="points tight" style="left:29px;top:187px;width:500px;font-size:7.6px;line-height:1.15">
    <li style="margin-bottom:2.5px"><b>Effective Time</b> is the time when the equipment is doing its productive activities</li>
    <li style="margin-bottom:2.5px">It excludes waiting/idle time that is included in operating time</li>
    <li>This waiting/idle, non-effective time is a part of the regular operation of the machine, but is not productive
      <ul><li>Shovel Hang</li><li>Truck wait @ dump or wait @ shovel</li></ul>
    </li>
    <li style="margin-bottom:2.5px">Effective Utilization % = Effective Time / Available Time</li>
    <li><b>OEE % = Effective Time / Calendar Time</b></li>
  </ul>
  <footer class="footer"><span class="brand">BRIMWELLS<span class="dot"></span></span><span class="legal">© 2024 Brimwells Mining Solutions Inc. Strictly Confidential</span><span class="num">9</span></footer>
</section>

<!-- 10 Operating Time -->
<section class="slide col-r row-5">
  <h2 class="slide-title" style="top:9px">TUM – Operating Time</h2>
  <div class="tum" style="top:49px;height:138px">
    <div class="cell r-cal c-cal">Calendar Time<small>0d 12 h 0 min</small></div>
    <div class="cell r-avail c-avail">Available Time<small>0d 12 h 0 min</small></div>
    <div class="cell r-avail c-down">Down<small>0d 12 h 0 min</small></div>
    <div class="cell r-half c-op">Operating Time<small>0d 12 h 0 min</small></div>
    <div class="cell r-full c-delay">Operating Delay<small>0d 12 h 0 min</small></div>
    <div class="cell r-full c-stby">Standby Time<small>0d 12 h 0 min</small></div>
    <div class="cell r-full c-un1">Unscheduled<small>0d 12 h 0 min</small></div>
    <div class="cell r-full c-un2">Unscheduled<small>0d 12 h 0 min</small></div>
  </div>
  <p style="position:absolute;left:23px;top:199px;width:245px;font-size:7.2px;line-height:1.1"><b>Operating Time</b> is the time where the equipment (or fleet) is working as planned</p>
  <ul class="points tight" style="left:23px;top:216px;width:250px;font-size:6.6px;line-height:1.05">
    <li>It excludes periods of standby and operating delays</li>
    <li>Standby time is typically time where the piece of equipment isn’t required to operate
      <ul><li style="font-size:5.8px">This could be because there isn’t work to do (No Shovel, No Muck)</li><li style="font-size:5.8px">It could also be because there is nobody to operate the machine (No Operator)</li></ul>
    </li>
  </ul>
  <ul class="points tight" style="left:283px;top:200px;width:240px;font-size:6.6px;line-height:1.05">
    <li>Operating Delay occurs when the equipment is required to operate but can’t perform it’s primary work function
      <ul><li style="font-size:5.8px">Fueling, Tramming, Moving</li><li style="font-size:5.8px">As a rule of thumb, if there is a ‘butt in the seat,’ it is considered an operating delay, not a standby</li></ul>
    </li>
    <li><b>Utilization % = Operating Time / Available Time</b></li>
    <li><b>Some sites refer to this as Use of Availability % or UofA %</b></li>
  </ul>
  <footer class="footer"><span class="brand">BRIMWELLS<span class="dot"></span></span><span class="legal">© 2024 Brimwells Mining Solutions Inc. Strictly Confidential</span><span class="num">10</span></footer>
</section>

</body>
</html>
```